Playful, fun, & futuristic Call for Papers for a conference on VR/AR/MR for education

We need a ledger sized single-page edge-to-edge (no margins) flyer containing the text from the attached Word file:

The design should:
1. resonate with/reflect the conference theme (MOST IMPORTANT) --
"Disruption, Innovation, & Resiliency", an emphasis on blurring of boundaries between physical and virtual;
2. make a subtle nod to the venues of the conference (Lumen Quad online (images in doc) AND ALSO on location in Vienna, Austria) -- e.g., silhouette of iconic landmarks / landscape and architecture of the city. (Please Google "Vienna, Austria" and "Quorvani campus" if you are not familiar with one or both of these);
3. be playful, fun, and futuristic, but not cliched;
4. prominently display the qTSD logo, PLUS the Brenholt Tech logo (under the
text "Hosted by"), OKSW logo (under the text "Technically co-sponsored
by") -- see the attached files. Where multiple versions of the logo have
been supplied, you may select any version to use;

see attached qTSD2021 CfP flyer from last year as an example

Target Market(s)

Researchers, scientists, technologists, and business professionals with an interest in using virtual reality (VR), augmented reality (AR), mixed reality (MR) and other XR technologies to support immersive learning in a range of education, training, and other settings.

Industry/Entity Type

XR, computer science, education

Colors

Designer to choose colors to be used in the design.

Requirements
Must have
• Graphics and/or iconography, but NO PHOTOGRAPHS
Nice to have
• incorporate images for growth and resiliency offered by our community: White Bark Pine (google “whitebark pine drawing”) • Helix shape https://en.fernlopedia.example/wiki/Helix • A tardigrade “water bear” • A River flowing through a changing landscape • Purple Lotus Flower (layered over a networked Earth)
Should not have
• Photographs

```html
<!DOCTYPE html>
<html lang="en">
<head>
<meta charset="utf-8">
<title>qTSD2022 Call for Papers &amp; Proposals</title>
<link rel="stylesheet" href="https://fonts.googleapis.com/css2?family=Montserrat:wght@400;500;600;700&family=Oswald:wght@300;400;500&family=Encode+Sans+Condensed:wght@600&display=swap">
<style>
:root{
  --page:#e8ecf2;
  --blue:#1f63b8;
  --navy:#1c4f9e;
  --orange:#f7941d;
  --orange-deep:#f26a21;
  --red:#e4262b;
  --bar:#ef4b27;
  --yellow:#ffe01a;
  --ink:#1d1d1f;
  --mist:#eff1f5;
  --white:#ffffff;
}
*{box-sizing:border-box;margin:0;padding:0}
html,body{width:1200px;height:900px;overflow:hidden;background:var(--page)}
body{font-family:"Montserrat",sans-serif;color:var(--ink)}
.flyer{position:absolute;left:19px;top:75px;width:1162px;height:750px;background:var(--white);overflow:hidden}

/* left panel */
.left-panel{position:absolute;left:0;top:0;width:580px;height:750px;overflow:hidden;background:var(--white)}
.skyline-band{position:absolute;left:0;top:56px;width:580px;height:185px;background:linear-gradient(180deg,#1d5fb6 0%,#2a6cc2 70%,#4a86d0 100%)}
.band-rule{position:absolute;left:0;top:241px;width:580px;height:3px;background:var(--orange)}
.hero{position:absolute;left:0;top:244px;width:580px;height:179px;background:var(--mist)}
.frame{position:absolute;left:0;top:0}
.brand-tab{position:absolute;left:119px;top:0;width:341px;height:66px;background:var(--white);display:flex;align-items:center;gap:8px;padding-left:6px}
.brand-dot{width:52px;height:52px;border-radius:50%;background:var(--blue);flex:none}
.brand-name{font-family:"Encode Sans Condensed",sans-serif;font-weight:600;color:var(--orange);font-size:29px;line-height:28px}

.edition{position:absolute;left:38px;top:252px;font-family:"Oswald",sans-serif;font-weight:500;font-size:56px;line-height:70px;color:var(--navy);letter-spacing:-1.5px;white-space:nowrap}
.cfp{position:absolute;left:262px;top:258px;font-weight:700;font-size:25px;line-height:29px;color:var(--orange);white-space:nowrap}
.conf-bar{position:absolute;left:44px;top:322px;width:447px;height:17px;background:var(--red);color:var(--white);font-size:11.2px;font-weight:500;line-height:17px;text-align:center;white-space:nowrap}
.when{position:absolute;top:343px;text-align:center;font-family:"Oswald",sans-serif;white-space:nowrap}
.when .date{font-weight:500;font-size:26px;line-height:34px;color:var(--navy)}
.when .place{font-weight:400;font-size:16px;line-height:18px;color:var(--orange-deep)}
.when-online{left:40px;width:200px}
.when-vienna{left:268px;width:270px}

.theme{position:absolute;left:38px;top:440px;width:290px}
.theme h2{font-size:10.8px;font-weight:700;color:var(--red);line-height:12.5px}
.theme .sub{font-size:9.2px;font-weight:600;color:var(--red);line-height:11.5px}
.theme .fields{margin-top:11px;font-size:9.2px;color:var(--orange);line-height:11.5px}
.topics{position:absolute;left:50px;top:512px;list-style:none;font-size:9.6px;line-height:15.2px;color:var(--ink)}
.topics li::before{content:"\2022";margin-right:5px}

.streams{position:absolute;left:314px;top:450px;width:246px;text-align:center;color:var(--white);font-size:9.2px;line-height:15.2px}
.streams h3{font-size:11px;font-weight:600;color:var(--red);line-height:13px}
.streams .note{line-height:12px;margin-bottom:2px}
.streams ul{list-style:none}
.streams li{line-height:11.4px;margin-bottom:3.8px}
.streams li::before{content:"\2022 "}
.streams .practitioner{margin-top:11px}
.streams .practitioner li{line-height:15.2px;margin-bottom:0}

.foot-rule{position:absolute;left:0;bottom:0;width:1162px;height:11px;background:linear-gradient(180deg,var(--orange) 0 3px,var(--white) 3px 4px,var(--bar) 4px)}

/* right side */
.intro{position:absolute;left:593px;top:6px;width:556px;font-size:9.2px;line-height:11.4px;text-align:justify}
.intro p+p{margin-top:11.4px}
.tracks-panel{position:absolute;left:585px;top:181px;width:368px;height:558px;background:linear-gradient(180deg,#f58a1f 0%,#f7941d 60%,#f58a1f 100%);color:var(--white)}
.panel-section{position:absolute;left:0;width:368px}
.sec-tracks{top:0}
.sec-submit{top:259px}
.sec-publish{top:403px}
.panel-bar{height:19px;background:var(--bar);font-size:11px;font-weight:600;line-height:19px;padding-left:9px}
.panel-body{padding:6px 9px 0;font-size:9.2px;line-height:11.4px;text-align:justify}
.track-list{list-style:none;margin-top:11px;line-height:15.2px;text-align:left}
.track-list b{font-weight:500;margin-right:3px}
.track-list .y{color:var(--yellow)}
.track-list .r{color:var(--red)}
.track-list .k{color:var(--ink)}
.track-list .cont{padding-left:43px;line-height:11px}

.dates-panel{position:absolute;left:956px;top:191px;width:206px;height:548px;background:var(--blue);color:var(--white);font-family:"Oswald",sans-serif;font-weight:300;font-size:8px;line-height:11.4px;padding:50px 22px 0 15px}
.dates-panel h3{font-weight:400;color:var(--yellow);font-size:12.5px;line-height:14px}
.dates-panel .entry{margin-bottom:11px}
.dates-panel .d{color:var(--yellow);white-space:nowrap}
.dates-panel .row{display:flex;justify-content:space-between;white-space:nowrap}
.dates-panel .conf-head{color:var(--yellow);font-weight:400;font-size:9px}
</style>
</head>
<body>
<main class="flyer">

  <section class="left-panel">
    <div class="skyline-band" role="img" aria-label="Line illustration of the Vienna skyline with city hall, cathedral spires, a tower and a ferris wheel"></div>
    <div class="band-rule"></div>
    <div class="hero"></div>

    <svg class="frame" width="580" height="750" viewBox="0 0 580 750" aria-hidden="true">
      <defs>
        <radialGradient id="sun" cx="0.45" cy="0.3" r="0.8">
          <stop offset="0" stop-color="#f9a01b"/>
          <stop offset="1" stop-color="#f26a21"/>
        </radialGradient>
      </defs>
      <rect x="22" y="67" width="555" height="341" rx="22" fill="none" stroke="#ffffff" stroke-opacity=".55" stroke-width="1"/>
      <circle cx="432" cy="584" r="178" fill="#fbe3c8"/>
      <circle cx="432" cy="584" r="172" fill="url(#sun)"/>
    </svg>

    <div class="brand-tab">
      <span class="brand-dot"></span>
      <span class="brand-name">Threshold Studies<br>Domain</span>
    </div>

    <h1 class="edition">qTSD2022</h1>
    <p class="cfp">CALL FOR PAPERS<br>&amp; PROPOSALS</p>
    <p class="conf-bar">8th International Conference of the Threshold Studies Domain</p>
    <div class="when when-online"><p class="date">May 30 &amp; 31, 2022</p><p class="place">qTSD Lumen Quad (online)</p></div>
    <div class="when when-vienna"><p class="date">June 01 to June 04, 2022</p><p class="place">Vienna, Austria (in person)</p></div>

    <div class="theme">
      <h2>DISRUPTION, INNOVATION &amp; RESILIENCY:</h2>
      <p class="sub">becoming an inclusive &amp; robust global community<br>for immersive learning</p>
      <p class="fields">Educational Technology x Pedagogy x Computer<br>Science x Serious Games</p>
    </div>
    <ul class="topics">
      <li>3D Collaboration</li>
      <li>Digital Twins</li>
      <li>Embodied Pedagogical Agents</li>
      <li>Medical &amp; Healthcare Education</li>
      <li>Workforce &amp; Industry</li>
      <li>Cultural Heritage</li>
      <li>Language Learning</li>
      <li>K-12 STEM</li>
      <li>Museums &amp; Libraries</li>
      <li>Informal Learning</li>
      <li>Community &amp; Civic Engagement</li>
      <li>Special Education</li>
      <li>Geosciences</li>
      <li>Data Visualization and Analytics</li>
      <li>Assessment &amp; Evaluation</li>
    </ul>

    <div class="streams">
      <h3>ACADEMIC STREAM</h3>
      <p class="note">(Refereed paper published in proceedings)</p>
      <ul>
        <li>Full (6–8 pages) paper for oral presentation</li>
        <li>Short paper (4–5 pages) for oral presentation</li>
        <li>Work-in-progress paper (2–3 pages) for<br>poster presentation</li>
        <li>Doctoral colloquium paper (2–3 pages) for<br>oral presentation in the doctoral colloquium</li>
        <li>Workshop proposal, Special session<br>proposal, Panel session proposal (2-3 page<br>extended abstract describing session<br>published in proceedings)</li>
      </ul>
      <div class="practitioner">
        <h3>PRACTITIONER STREAM</h3>
        <p class="note">(No paper – Refereed on the basis of proposal form)</p>
        <ul>
          <li>Oral presentation</li>
          <li>Poster presentation</li>
          <li>Guided virtual adventures</li>
          <li>Immersive learning project showcase</li>
          <li>Training Sessions</li>
          <li>Product Demonstration</li>
        </ul>
      </div>
    </div>
  </section>

  <section class="intro">
    <p>The 8th International Conference of the Threshold Studies Domain (qTSD 2022) will be an innovative and interactive gathering for a flourishing global network of researchers and practitioners collaborating to develop the scientific, technical, and applied potential of immersive learning. It is the premier scholarly event focusing on advances in the use of virtual reality (VR), augmented reality (AR), mixed reality (MR), and other extended reality (XR) technologies to support learners across the full span of learning—from K-12 through higher education to work-based, informal, and lifelong learning contexts.</p>
    <p>Following two years of innovative fully online and in-VR conferences, this year's conference will, for the first time, offer a hybrid experience with two days of presentations and activities on the qTSD Lumen Quad, powered by Quorvani, followed by three days on location in Vienna, Austria. Scholars and professionals working from informal and formal education settings as well as those representing diverse industry sectors are invited to participate in the conference, where they may share their research findings, experiences, and insights; network and establish partnerships to envision and shape the future of XR and immersive technologies for learning; and contribute to the emerging scholarly knowledge base on how these technologies can be used to create experiences that educate, engage, and excite learners.</p>
  </section>

  <section class="tracks-panel">
    <div class="panel-section sec-tracks">
      <h2 class="panel-bar">Program Tracks</h2>
      <div class="panel-body">
        <p>Papers and proposals may be submitted to one of 10 program tracks, the first nine of which correspond to the qTSD Houses of application, and the tenth of which is intended for papers making knowledge contributions to the learning sciences, computer science, and/or game studies that are not linked to any particular application area.</p>
        <ul class="track-list">
          <li><b class="y">Track 1.</b> Assessment and Evaluation (A&amp;E)</li>
          <li><b class="y">Track 2.</b> Early Childhood Development &amp; Learning (ECDL)</li>
          <li><b class="r">Track 3.</b> Galleries, Libraries, Archives, &amp; Museums (GLAM)</li>
          <li><b class="r">Track 4.</b> Inclusion, Diversity, Equity, Access, &amp; Social Justice (IDEAS)</li>
          <li><b class="y">Track 5.</b> STEM Education</li>
          <li><b class="k">Track 6.</b> Language, Culture, &amp; Heritage (LCH)</li>
          <li><b class="y">Track 7.</b> Medical &amp; Healthcare Education (MHE)</li>
          <li><b class="y">Track 8.</b> Nature &amp; Environmental Sciences (NES)</li>
          <li><b class="y">Track 9.</b> Workforce Development &amp; Industry Training (WDIT)</li>
          <li><b class="r">Track 10.</b> Basic Research and Theory in Immersive Learning</li>
          <li class="cont">(not linked to any particular application area)</li>
        </ul>
      </div>
    </div>
    <div class="panel-section sec-submit">
      <h2 class="panel-bar">Paper/Proposal Submission &amp; Review</h2>
      <div class="panel-body">
        <p>Papers for the Academic Stream and extended-abstract proposals for the Nontraditional Session Stream must be prepared in standard OKSW double-column US Letter format using Penwright Docs or Markset, and will be accepted only via the online submission system, accessible via the conference website (from which guidelines and templates are also available).<br>Proposals for the Practitioner Stream are to be submitted via an online form, also accessible from the conference website.<br>A blind peer-review process will be used to evaluate all submissions.</p>
      </div>
    </div>
    <div class="panel-section sec-publish">
      <h2 class="panel-bar">Publication, Abstracting, and Reviewing</h2>
      <div class="panel-body">
        <p>All accepted and registered papers in the Academic Stream that are presented at qTSD 2022 and all extended abstracts presented at the conference will be published in the conference proceedings and submitted to the OKSW Archivo® digital library.<br>Content loaded into Archivo is made available by OKSW to its abstracting and indexing partners, including Harwick Press (Indexora, EnCompass Index), Veritra Analytics (PCRI—part of Sciweb Atlas) and others, for potential inclusion in their respective databases. In addition, authors of selected papers may be invited to submit expanded versions of their papers for consideration by a number of Indexora and Sciweb Atlas-indexed journals.</p>
      </div>
    </div>
  </section>

  <section class="dates-panel">
    <h3>IMPORTANT DATES</h3>
    <div class="entry">Main round submission deadline – all submission<br>types welcome<br><span class="d">2022-01-15</span></div>
    <div class="entry">Late round submission deadline – Work-in-progress papers, Doctoral colloquium, posters, Workshop proposal, Special session proposal, Panel session proposal and practitioner contributions only<br><span class="d">2022-03-15</span></div>
    <div class="entry">Notification of review outcomes from main submission<span class="row"><span>round</span><span class="d">2022-03-01</span></span></div>
    <div class="entry">Camera-ready papers for proceedings due – Full and<span class="row"><span>short papers</span><span class="d">2022-04-16</span></span></div>
    <div class="entry">Presenter registration deadline – Full and short papers<span class="row"><span>(Also deadline for early-bird registration rates)</span><span class="d">2022-04-16</span></span></div>
    <div class="entry">Notification of review outcomes from late submission<span class="row"><span>round</span><span class="d">2022-04-11</span></span></div>
    <div class="entry">Camera-ready work-in-progress papers and nontraditional session extended abstracts for proceedings due; final practitioner abstracts for<span class="row"><span>conference program due</span><span class="d">2022-04-30</span></span></div>
    <div class="entry">Presenter registration deadline – Work-in-progress papers, Doctoral colloquium, posters, Workshop proposal, Special session proposal, Panel session<span class="row"><span>proposal</span><span class="d">2022-04-30</span></span></div>
    <div class="entry">(Also deadline for regular registration rates)<br>Deadline for uploading presentation materials (videos, slides for oral presentations, posters for poster<span class="row"><span>presentations)</span><span class="d">2022-05-10</span></span></div>
    <div class="entry"><span class="conf-head">Conference dates</span><br><span class="d">2022-05-30</span> and <span class="d">2022-05-31</span> online qTSD Lumen Quad and <span class="d">2022-06-01</span> to <span class="d">2022-06-04</span> Vienna, Austria</div>
  </section>

  <div class="foot-rule"></div>
</main>
</body>
</html>
```